Enhancement Of Draft Website - www.skyvoltbridge.net

The website www.skyvoltbridge.net exists but needs further development. With the exception of a small number of pages, the website is populated with the majority of content it requires. I would like a designer to review the design of the website and propose an enhanced design paying particular consideration to the following:

-Setting an appropriate colour scheme that matches with the company logo
-Ensuring the company logo is displayed appropriately on the website
-Making any other appropriate adjustments (through the selection of another theme / the customisation of the existing template) that improve the experience of the user on the website

An XML export file from the existing website is attached.

Target Market(s)

Specialist website targeting engineers working in aerospace companies

Industry/Entity Type

Engineer

Font styles to use
Sans Serif

Requirements
Must have
• Responsive design working across platforms. Contact form. Ease of use.

```html
<!DOCTYPE html>
<html lang="en">
<head>
<meta charset="utf-8">
<title>skyvoltbridge – High Voltage Training</title>
<link rel="stylesheet" href="https://fonts.googleapis.com/css2?family=Montserrat:wght@300;400;500;600;700&display=swap">
<style>
  :root {
    --brand: #3e6d98;
    --brand-dark: #2c4f72;
    --ink: #2b2f33;
    --muted: #8a8f94;
    --nav: #3a3f44;
    --line: #e4e7ea;
    --white: #ffffff;
    --footer: #3d6c97;
    --footer-line: rgba(255,255,255,0.25);
  }
  * { box-sizing: border-box; margin: 0; padding: 0; }
  html, body { width: 1200px; height: 2528px; overflow: hidden; }
  body {
    position: relative;
    background: var(--white);
    font-family: "Montserrat", Arial, sans-serif;
    color: var(--ink);
  }
  .abs { position: absolute; }
  .center { text-align: center; left: 0; width: 1200px; }

  /* Header */
  .site-header { position: absolute; top: 0; left: 0; width: 1200px; height: 121px; background: var(--white); }
  .brand { position: absolute; left: 98px; top: 46px; display: flex; align-items: center; gap: 12px; }
  .brand-mark { width: 30px; height: 30px; background: var(--brand-dark); }
  .brand-name { font-size: 31px; font-weight: 500; color: var(--brand-dark); letter-spacing: -0.5px; }
  .main-nav { position: absolute; top: 57px; right: 96px; display: flex; gap: 23px; font-size: 13.5px; color: var(--nav); text-transform: uppercase; }
  .main-nav span { display: flex; align-items: center; gap: 4px; position: relative; }
  .main-nav .active { color: var(--brand); }
  .main-nav .active::after { content: ""; position: absolute; left: -2px; right: -2px; top: 28px; height: 3px; background: var(--brand); }
  .caret { width: 8px; height: 6px; }

  /* Hero */
  .hero { position: absolute; top: 121px; left: 0; width: 1200px; height: 600px;
    background: linear-gradient(180deg, #1f3d55 0%, #3b5e78 35%, #6d8497 65%, #9aa6b0 100%); }
  .hero-curve { position: absolute; left: 0; top: 660px; width: 1200px; height: 62px; }
  .hero-title { top: 295px; font-size: 58px; font-weight: 700; color: var(--white); letter-spacing: 1px; }
  .hero-sub { top: 368px; font-size: 19.5px; font-weight: 300; color: #eef2f5; line-height: 26px; }
  .dots { position: absolute; top: 636px; left: 562px; display: flex; gap: 3px; }
  .dot { width: 16px; height: 16px; border-radius: 50%; background: var(--white); border: 2px solid var(--white); }
  .dot.current { background: transparent; }

  /* Welcome */
  .welcome-title { top: 742px; font-size: 44px; font-weight: 300; color: var(--brand); }
  .welcome-text { top: 810px; font-size: 18.5px; font-weight: 300; color: #555a5f; line-height: 27px; }
  .divider { position: absolute; top: 893px; left: 300px; width: 600px; height: 1px; background: var(--line); }

  .service { position: absolute; top: 923px; width: 320px; text-align: center; }
  .service-badge { width: 152px; height: 152px; border-radius: 50%; border: 3px solid #e9edf1; margin: 0 auto; display: flex; align-items: center; justify-content: center; }
  .service-badge div { width: 140px; height: 140px; border-radius: 50%; background: var(--brand); }
  .service-title { margin-top: 18px; font-size: 21px; font-weight: 400; color: var(--ink); letter-spacing: 0.5px; }
  .service-text { margin-top: 12px; font-size: 14.5px; font-weight: 300; color: #7a7f84; line-height: 23px; }

  /* About */
  .about { position: absolute; top: 1240px; left: 0; width: 1200px; height: 411px;
    background: linear-gradient(180deg, #4b7aa3 0%, #4f7ea7 55%, #5585ad 100%); }
  .about-title { top: 1284px; font-size: 48px; font-weight: 300; color: var(--white); }
  .about-text { top: 1362px; font-size: 19.5px; font-weight: 400; color: var(--white); line-height: 28px; }
  .about-reg { top: 1437px; font-size: 19.5px; font-weight: 300; color: var(--white); line-height: 28px; }
  .btn-outline { position: absolute; top: 1540px; left: 490px; width: 219px; height: 51px; border: 1.5px solid rgba(255,255,255,0.85);
    color: var(--white); font-size: 19px; font-weight: 500; letter-spacing: 1px; display: flex; align-items: center; justify-content: center; }

  /* HV basics */
  .basics-title { top: 1692px; font-size: 29px; font-weight: 600; color: var(--ink); letter-spacing: 1px; }
  .basics-title b { color: var(--brand); font-weight: 600; }
  .slider-arrows { position: absolute; top: 1697px; left: 1041px; display: flex; gap: 4px; }
  .slider-arrows svg { width: 28px; height: 28px; }
  .card { position: absolute; top: 1773px; width: 315px; height: 380px; }
  .card-photo { width: 315px; height: 182px; }
  .card-title { margin: 34px 4px 0; font-size: 19.5px; font-weight: 400; color: var(--ink); line-height: 22px; text-transform: uppercase; }
  .card-text { margin: 12px 4px 0; font-size: 13.5px; font-weight: 300; color: #7d8287; line-height: 22px; }
  .btn-small { position: absolute; top: 332px; left: 4px; width: 124px; height: 39px; background: var(--brand); color: var(--white);
    font-size: 14.5px; font-weight: 400; display: flex; align-items: center; justify-content: center; gap: 8px; }

  /* Footer */
  .site-footer { position: absolute; top: 2199px; left: 0; width: 1200px; height: 329px; background: var(--footer); color: var(--white); }
  .f-col { position: absolute; top: 46px; }
  .f-col h4 { font-size: 16.5px; font-weight: 600; letter-spacing: 0.5px; margin-bottom: 14px; }
  .f-col li { list-style: none; font-size: 13.5px; font-weight: 400; line-height: 30px; color: #e8eef4; }
  .f-col li.icon { display: flex; align-items: center; gap: 10px; }
  .f-sep { position: absolute; top: 44px; width: 1px; height: 198px; background: var(--footer-line); }
  .social { display: flex; gap: 5px; margin-top: 12px; }
  .social span { width: 38px; height: 38px; border-radius: 50%; border: 2px solid var(--white); background: rgba(255,255,255,0.18); }
  .f-rule { position: absolute; top: 258px; left: 101px; width: 999px; height: 1px; background: var(--footer-line); }
  .f-copy { position: absolute; top: 280px; left: 101px; font-size: 13px; color: #e8eef4; }
</style>
</head>
<body>

<header class="site-header">
  <div class="brand"><span class="brand-mark"></span><span class="brand-name">skyvoltbridge</span></div>
  <nav class="main-nav">
    <span class="active">Home</span>
    <span>Engineering <svg class="caret" viewBox="0 0 8 6"><path d="M1 1l3 3 3-3" fill="none" stroke="currentColor" stroke-width="1.3"/></svg></span>
    <span>Testing <svg class="caret" viewBox="0 0 8 6"><path d="M1 1l3 3 3-3" fill="none" stroke="currentColor" stroke-width="1.3"/></svg></span>
    <span>Training <svg class="caret" viewBox="0 0 8 6"><path d="M1 1l3 3 3-3" fill="none" stroke="currentColor" stroke-width="1.3"/></svg></span>
    <span>HV Basics <svg class="caret" viewBox="0 0 8 6"><path d="M1 1l3 3 3-3" fill="none" stroke="currentColor" stroke-width="1.3"/></svg></span>
    <span>About Us</span>
    <span>Contact Us</span>
  </nav>
</header>

<section class="hero" role="img" aria-label="Photo of a sleek high-speed train waiting under a curved glass station roof"></section>
<svg class="hero-curve" viewBox="0 0 1200 62" preserveAspectRatio="none"><path d="M0 62 L0 42 Q600 -40 1200 42 L1200 62 Z" fill="#ffffff"/></svg>
<h1 class="abs center hero-title">HIGH VOLTAGE TRAINING</h1>
<p class="abs center hero-sub">Essential knowledge for those involved in the design, operation and maintenance of HV systems<br>in aerospace applications.</p>
<div class="dots"><span class="dot current"></span><span class="dot"></span><span class="dot"></span><span class="dot"></span></div>

<h2 class="abs center welcome-title">Welcome to skyvoltbridge</h2>
<p class="abs center welcome-text">Essential knowledge for those involved in the design, operation and maintenance of HV systems<br>in aerospace applications.</p>
<div class="divider"></div>

<div class="service" style="left:84px">
  <div class="service-badge"><div role="img" aria-label="Gears icon"></div></div>
  <h3 class="service-title">ENGINEERING</h3>
  <p class="service-text">Supporting the design of new HV systems<br>and components for use in aerospace<br>environments</p>
</div>
<div class="service" style="left:438px">
  <div class="service-badge"><div role="img" aria-label="Jet aircraft icon"></div></div>
  <h3 class="service-title">TESTING</h3>
  <p class="service-text">Access to a full range of testing services<br>to validate the performance of HV<br>systems</p>
</div>
<div class="service" style="left:795px">
  <div class="service-badge"><div role="img" aria-label="Group of people icon"></div></div>
  <h3 class="service-title">TRAINING</h3>
  <p class="service-text">Online and face to face training provision<br>to support your workforce</p>
</div>

<section class="about" role="img" aria-label="Faded photo of an aircraft in flight under a blue overlay"></section>
<h2 class="abs center about-title">About Us</h2>
<p class="abs center about-text">Essential knowledge for those involved in the design, operation and maintenance of HV<br>systems in aerospace applications.</p>
<p class="abs center about-reg">Voltbridge Design Ltd trading as skyvoltbridge - Registered in England and Wales,<br>Company number 0472913</p>
<div class="btn-outline">READ MORE</div>

<h2 class="abs center basics-title">HV <b>BASICS</b></h2>
<div class="slider-arrows">
  <svg viewBox="0 0 28 28"><circle cx="14" cy="14" r="13" fill="#e6e8ea"/><path d="M16 9l-5 5 5 5" fill="none" stroke="#666" stroke-width="1.6"/></svg>
  <svg viewBox="0 0 28 28"><circle cx="14" cy="14" r="13" fill="#e6e8ea"/><path d="M12 9l5 5-5 5" fill="none" stroke="#666" stroke-width="1.6"/></svg>
</div>

<article class="card" style="left:99px">
  <div class="card-photo" role="img" aria-label="Photo of electrical arcs discharging between two electrodes" style="background:linear-gradient(180deg,#2a2d3a,#4a4a5e 60%,#1c1d24)"></div>
  <h3 class="card-title">Electrical Discharge<br>Types</h3>
  <p class="card-text">Essential knowledge for those involved in<br>the design, operation and maintenance.</p>
  <div class="btn-small">Read More <svg width="7" height="10" viewBox="0 0 7 10"><path d="M1 1l4 4-4 4" fill="none" stroke="#fff" stroke-width="1.5"/></svg></div>
</article>
<article class="card" style="left:441px">
  <div class="card-photo" role="img" aria-label="Close-up photo of connector pins and a blue header on a circuit board" style="background:linear-gradient(135deg,#3b3a38,#6e6a62 45%,#3f6fb5 75%,#2a2a2a)"></div>
  <h3 class="card-title">Clearances</h3>
  <p class="card-text">Essential knowledge for those involved in<br>the design, operation and maintenance of<br>HV systems in aerospace applications.</p>
  <div class="btn-small">Read More <svg width="7" height="10" viewBox="0 0 7 10"><path d="M1 1l4 4-4 4" fill="none" stroke="#fff" stroke-width="1.5"/></svg></div>
</article>
<article class="card" style="left:785px">
  <div class="card-photo" role="img" aria-label="Photo of grey terminal blocks with red wires" style="background:linear-gradient(180deg,#b9b2b0,#d5d6d8 40%,#9fa2a6)"></div>
  <h3 class="card-title">Creepage Distances</h3>
  <p class="card-text">Essential knowledge for those involved in<br>the design, operation and maintenance of<br>HV systems in aerospace applications.</p>
  <div class="btn-small">Read More <svg width="7" height="10" viewBox="0 0 7 10"><path d="M1 1l4 4-4 4" fill="none" stroke="#fff" stroke-width="1.5"/></svg></div>
</article>

<footer class="site-footer">
  <div class="f-col" style="left:101px"><h4>COMPANY</h4><ul><li>Engineering</li><li>Testing</li><li>Training</li><li>HV Basics</li><li>Contact Us</li></ul></div>
  <div class="f-sep" style="left:244px"></div>
  <div class="f-col" style="left:275px"><h4>TESTING</h4><ul><li>Test Facilities</li><li>Qualification Testing</li><li>Quality Management</li><li>Production Testing</li></ul></div>
  <div class="f-sep" style="left:452px"></div>
  <div class="f-col" style="left:489px"><h4>GET IN TOUCH</h4><ul>
    <li class="icon"><svg width="13" height="13" viewBox="0 0 24 24"><path d="M6.6 10.8a15 15 0 006.6 6.6l2.2-2.2c.3-.3.7-.4 1-.2 1.1.4 2.3.6 3.6.6.6 0 1 .4 1 1V20c0 .6-.4 1-1 1C10.6 21 3 13.4 3 4c0-.6.4-1 1-1h3.5c.6 0 1 .4 1 1 0 1.3.2 2.5.6 3.6.1.3 0 .7-.2 1z" fill="#fff"/></svg>Call us on (01) 23456789</li>
    <li class="icon"><svg width="13" height="11" viewBox="0 0 24 18"><rect width="24" height="18" rx="2" fill="#fff"/><path d="M1 2l11 8 11-8" fill="none" stroke="#3d6c97" stroke-width="2"/></svg>info@domainname.com</li>
  </ul></div>
  <div class="f-sep" style="left:725px"></div>
  <div class="f-col" style="left:762px"><h4>WHY US</h4><ul><li>Customers</li><li>Team</li><li>FAQ</li><li>Contact</li></ul></div>
  <div class="f-sep" style="left:881px"></div>
  <div class="f-col" style="left:925px"><h4>FOLLOW US</h4><ul><li>Please connect with us on</li></ul>
    <div class="social"><span></span><span></span><span></span><span></span></div>
  </div>
  <div class="f-rule"></div>
  <p class="f-copy">© 2016 Company Name &nbsp;All right reserved &nbsp;Term of Use</p>
</footer>

</body>
</html>
```